Real estate business needing a creative mind!

Have a real estate business called Brightwell Estates LLC. I need some business card with custom logo. That logo can be an intricate design of a house or houses. Maybe some blue and orange colors, maybe the business name in orange. Some thing that leaves a wow impression to the holder. Or just surprise me! Must have business name, name, email and phone number.

Target Market(s)

Property sellers and real estate professionals

Industry/Entity Type

Real estate

Contact Information for Business Card

Want it to stand out but also be professional.

Colors

Designer to choose colors to be used in the design.

Requirements
Must have
• Business name Brightwell Estates. My name which is Dalton Meese. The business email which is Brightwellestates1@novamail.example. The phone number which is 555-014-2297
Nice to have
• Could be a logo of the name over some mountain houses being that we live by the Smokey mountains. Could have a sun if it looks ok?

```html
<!DOCTYPE html>
<html lang="en">
<head>
<meta charset="utf-8">
<title>Brightwell Estates – Business Cards</title>
<link rel="stylesheet" href="https://fonts.googleapis.com/css2?family=Montserrat:wght@400;600;800&display=swap">
<style>
  :root {
    --backdrop: #cdcdcf;
    --navy: #002a7f;
    --sky: #1a8cf0;
    --sun: #f8ae08;
    --paper: #ffffff;
  }
  * { box-sizing: border-box; margin: 0; padding: 0; }
  html, body {
    width: 1200px; height: 900px; overflow: hidden;
    background: var(--backdrop);
    font-family: "Montserrat", sans-serif;
  }
  .sheet {
    width: 1200px; height: 900px;
    display: flex; align-items: center; justify-content: center; gap: 40px;
  }
  .card {
    position: relative;
    width: 540px; height: 309px;
    overflow: hidden;
    box-shadow: 0 10px 28px rgba(0,0,0,0.22);
  }
  .card--front { background: var(--paper); }
  .card--back { background: var(--navy); display: flex; align-items: center; justify-content: center; }
  .card__bands { position: absolute; inset: 0; width: 100%; height: 100%; }
  .brand {
    display: flex; align-items: center; gap: 10px;
    font-weight: 800; letter-spacing: 0.02em; text-transform: uppercase;
  }
  .brand__dot { border-radius: 50%; background: var(--sun); flex: none; }
  .brand__name { line-height: 1.05; }
  .card--front .brand {
    position: absolute; left: 30px; top: 30px;
    color: var(--navy); font-size: 20px;
  }
  .card--front .brand__name { display: flex; flex-direction: column; }
  .card--front .brand__dot { width: 30px; height: 30px; }
  .card--back .brand { color: var(--paper); font-size: 34px; }
  .card--back .brand__dot { width: 40px; height: 40px; }
  .contact {
    position: absolute; right: 26px; bottom: 34px;
    text-align: right; color: var(--paper);
  }
  .contact__name {
    font-weight: 600; font-size: 34px; letter-spacing: 0.01em;
    text-transform: uppercase; line-height: 1.1; margin-bottom: 12px;
  }
  .contact__line { font-weight: 400; font-size: 13px; line-height: 1.5; }
</style>
</head>
<body>
  <main class="sheet">
    <section class="card card--front">
      <svg class="card__bands" viewBox="0 0 540 309" preserveAspectRatio="none" aria-hidden="true">
        <polygon points="322,0 344,0 136,309 126,309" fill="var(--sun)"/>
        <polygon points="344,0 366,0 144,309 136,309" fill="var(--sky)"/>
        <polygon points="366,0 540,0 540,309 144,309" fill="var(--navy)"/>
      </svg>
      <div class="brand">
        <span class="brand__dot"></span>
        <span class="brand__name"><span>Brightwell</span><span>Estates</span></span>
      </div>
      <div class="contact">
        <p class="contact__name">Dalton Meese</p>
        <p class="contact__line">555-014-2297</p>
        <p class="contact__line">Brightwellestates1@novamail.example</p>
      </div>
    </section>

    <section class="card card--back">
      <div class="brand">
        <span class="brand__dot"></span>
        <span class="brand__name">Brightwell Estates</span>
      </div>
    </section>
  </main>
</body>
</html>
```